Terra Swift Business Card Design

We need to improve the design of our current business card. We are a erosion control, hydro seeding company that serves many markets. We are attaching the current business card and our logo as reference. You may also visit our site at www.terraswiftllc.example to reference.

```html
<!DOCTYPE html>
<html lang="en">
<head>
<meta charset="utf-8">
<title>Terra Swift Business Card</title>
<link href="https://fonts.googleapis.com/css2?family=Open+Sans:wght@400;600;700;800&display=swap" rel="stylesheet">
<style>
  :root {
    --backdrop: #808080;
    --brand-green: #2fb26c;
    --brand-green-light: #3aa85f;
    --deep-green: #1f4a33;
    --paper: #f6f6f6;
    --ink: #111111;
    --band: #121212;
    --white: #ffffff;
  }
  * { margin: 0; padding: 0; box-sizing: border-box; }
  html, body { width: 1200px; height: 1000px; overflow: hidden; }
  body {
    background: var(--backdrop);
    font-family: "Open Sans", Arial, sans-serif;
    position: relative;
  }
  .card {
    position: absolute;
    left: 295px;
    width: 612px;
    height: 351px;
    border-radius: 28px;
    overflow: hidden;
    box-shadow: 0 10px 22px rgba(0,0,0,0.35);
  }
  .card-front {
    top: 120px;
    background: var(--brand-green);
    display: flex;
    align-items: center;
    justify-content: center;
    gap: 18px;
  }
  .front-mark {
    width: 34px; height: 34px;
    border-radius: 50%;
    background: var(--white);
  }
  .front-name {
    color: var(--white);
    font-weight: 800;
    font-size: 66px;
    letter-spacing: -1px;
  }
  .card-back {
    top: 512px;
    background: var(--paper);
  }
  .back-logo {
    position: absolute;
    left: 32px; top: 34px;
    display: flex; align-items: center; gap: 10px;
  }
  .back-logo .mark {
    width: 16px; height: 16px; border-radius: 50%;
    background: var(--deep-green);
  }
  .back-logo .name {
    color: var(--deep-green);
    font-weight: 800;
    font-size: 32px;
    letter-spacing: -0.5px;
  }
  .person {
    position: absolute;
    right: 65px; top: 40px;
    text-align: right;
    font-size: 16px;
    line-height: 21px;
  }
  .person-name { color: var(--deep-green); font-weight: 700; }
  .person-title { color: var(--brand-green-light); }
  .services {
    position: absolute;
    top: 123px;
    list-style: none;
    font-size: 14px;
    line-height: 17px;
    color: var(--ink);
  }
  .services li::before { content: "• "; }
  .col-1 { left: 19px; }
  .col-2 { left: 235px; }
  .col-3 { left: 429px; width: 170px; }
  .accent-rule {
    position: absolute;
    left: 0; right: 0; top: 281px;
    height: 4px;
    background: var(--brand-green);
  }
  .contact-band {
    position: absolute;
    left: 0; right: 0; top: 286px; bottom: 0;
    background: var(--band);
    color: var(--white);
    font-size: 14px;
    line-height: 17px;
  }
  .contact-block { position: absolute; top: 14px; text-align: center; }
  .contact-phone { left: 120px; width: 150px; }
  .contact-web { left: 320px; width: 200px; font-weight: 700; }
  .contact-phone strong { font-weight: 700; }
</style>
</head>
<body>
  <section class="card card-front" aria-label="Card front">
    <span class="front-mark"></span>
    <span class="front-name">Terra Swift</span>
  </section>

  <section class="card card-back" aria-label="Card back">
    <div class="back-logo">
      <span class="name">Terra Swift</span>
      <span class="mark"></span>
    </div>
    <div class="person">
      <div class="person-name">Dana Whitfield</div>
      <div class="person-title">Chief Operating Officer</div>
    </div>

    <ul class="services col-1">
      <li>Erosion Control Installation</li>
      <li>Seed and Straw</li>
      <li>Hydroseeding</li>
      <li>Compost Blankets</li>
      <li>Drill Seeding</li>
      <li>Erosion Control Blankets</li>
      <li>Turf Reinforcement Matting</li>
    </ul>
    <ul class="services col-2">
      <li>Custom Soil Amending</li>
      <li>Native, Pollinator</li>
      <li>Wetland Seeding</li>
      <li>Silt Fence</li>
      <li>Filter Sock</li>
      <li>Construction Entrances</li>
      <li>Clearing &amp; Grubbing</li>
    </ul>
    <ul class="services col-3">
      <li>Skimmer Basins</li>
      <li>Diversion Ditches</li>
      <li>Site Prep &amp; Grading</li>
      <li>Gravel Access Roads</li>
      <li>Laydown Construction &amp; Restoration</li>
    </ul>

    <div class="accent-rule"></div>
    <div class="contact-band">
      <div class="contact-block contact-phone">
        <div><strong>Phone:</strong> (555) 014-2286</div>
        <div><strong>Fax:</strong> (555) 014-2285</div>
      </div>
      <div class="contact-block contact-web">
        <div>info@terraswiftllc.example</div>
        <div>terraswiftllc.example</div>
      </div>
    </div>
  </section>
</body>
</html>
```